'Tarvel' a financial/crypto-currency exchange in the middle east

On the card we need 1) Name 2) title 3) email address 4) phone number using the same colors and theme as the logo. On one side we just want the logo and we want the whole card to be in blue (same blue as logo) with the logo in the back being white.
Industry/Entity Type
Financial

```html
<!DOCTYPE html>
<html lang="en">
<head>
<meta charset="utf-8">
<title>Tarvel Business Card</title>
<link href="https://fonts.googleapis.com/css2?family=Montserrat:wght@400;700&display=swap" rel="stylesheet">
<style>
  :root {
    --backdrop: #2b9bd7;
    --card-blue: #1a8fd0;
    --card-blue-light: #3ba6dc;
    --white: #ffffff;
  }
  html, body {
    margin: 0;
    padding: 0;
    width: 1200px;
    height: 900px;
    overflow: hidden;
    background: var(--backdrop);
    font-family: "Montserrat", sans-serif;
  }
  .stage {
    position: relative;
    width: 1200px;
    height: 900px;
  }
  .card {
    position: absolute;
    top: 214px;
    width: 270px;
    height: 472px;
    overflow: hidden;
    color: var(--white);
    background: linear-gradient(160deg, var(--card-blue) 0%, var(--card-blue-light) 30%, var(--card-blue) 70%);
    box-shadow: 0 2px 4px rgba(0, 0, 0, 0.25);
  }
  .card--front { left: 309px; }
  .card--back { left: 621px; }
  .corner-disc {
    position: absolute;
    width: 132px;
    height: 132px;
    border-radius: 50%;
    background: var(--white);
  }
  .card--front .corner-disc { left: 163px; top: -8px; }
  .card--back .corner-disc { left: 157px; top: 362px; }
  .person {
    position: absolute;
    left: 26px;
    top: 332px;
  }
  .person__name {
    margin: 0;
    font-size: 24px;
    font-weight: 700;
    line-height: 30px;
    letter-spacing: 0.2px;
  }
  .person__title {
    margin: 0;
    font-size: 16px;
    font-weight: 400;
    line-height: 20px;
  }
  .person__rule {
    width: 28px;
    height: 3px;
    background: var(--white);
    margin: 12px 0 10px;
  }
  .person__contact {
    margin: 0;
    font-size: 16px;
    font-weight: 400;
    line-height: 22px;
  }
  .brand {
    position: absolute;
    left: 35px;
    top: 208px;
    display: flex;
    align-items: center;
    gap: 12px;
  }
  .brand__dot {
    width: 58px;
    height: 58px;
    border-radius: 50%;
    background: var(--white);
  }
  .brand__name {
    font-size: 34px;
    font-weight: 700;
    letter-spacing: 0.5px;
  }
</style>
</head>
<body>
  <main class="stage">
    <section class="card card--front">
      <div class="corner-disc"></div>
      <div class="person">
        <p class="person__name">Omar Haddad</p>
        <p class="person__title">Founder &amp; CEO</p>
        <div class="person__rule"></div>
        <p class="person__contact">555.014.2290</p>
        <p class="person__contact">omar@tarvel.com</p>
      </div>
    </section>
    <section class="card card--back">
      <div class="brand">
        <div class="brand__dot"></div>
        <span class="brand__name">Tarvel</span>
      </div>
      <div class="corner-disc"></div>
    </section>
  </main>
</body>
</html>
```